Contemporary Media Company with Logo Needs Business Card Design

Need a modern card design for a full service digital media company using the logo included. Also want the info below on the card. Probably list the services on the card back to save space for the front. Want something contemporary to impress prospective clients. You may want to submit both a somewhat more conservative design, and then a more wild one.
General Info: (this phrase need not be on the card)
Tod Parvin
Founder and CEO
949-628-4513
tod@lumavantstudio.example
lumavantstudio.example
Services: (this word need not be on the card)
Content & Experience Strategy
Brand Development
Search Engine Optimization
Website Design
Website Operation
Social Media Integration
Complete Video Solutions
Industry/Entity Type
Business
Contact Information for Business Card
Tod Parvin
Founder and CEO
949-628-4513
tod@lumavantstudio.example
lumavantstudio.example
Brand Development
Website Design
Website Operation
Social Media Integration
Complete Video Solutions
Look and feel

```html
<!DOCTYPE html>
<html lang="en">
<head>
<meta charset="utf-8">
<title>Lumavant Studio — Business Card</title>
<link rel="stylesheet" href="https://fonts.googleapis.com/css2?family=Montserrat:wght@300;400;500&family=Open+Sans:wght@400;600&display=swap">
<style>
  :root {
    --backdrop: #eef0f0;
    --card-white: #ffffff;
    --band-dark: #262626;
    --brand-orange: #f07a1a;
    --brand-grey: #6d6d6d;
    --gold-light: #f6ec9a;
    --gold-deep: #d9c35a;
    --ink: #4a4a4a;
    --ink-light: #f2f2f2;
  }
  * { box-sizing: border-box; margin: 0; padding: 0; }
  html, body { width: 1200px; height: 1039px; overflow: hidden; }
  body {
    background: var(--backdrop);
    font-family: "Open Sans", Arial, sans-serif;
    position: relative;
  }
  .card {
    position: absolute;
    left: 250px;
    width: 700px;
    height: 400px;
    background: var(--card-white);
    box-shadow: 0 10px 28px rgba(0,0,0,0.12), 0 2px 4px rgba(0,0,0,0.08);
    overflow: hidden;
  }
  .card--front { top: 80px; }
  .card--back { top: 560px; }

  .brand {
    display: flex;
    align-items: center;
    gap: 16px;
    white-space: nowrap;
  }
  .brand__mark {
    flex: 0 0 auto;
    width: 34px;
    height: 34px;
    background: var(--brand-orange);
  }
  .brand__name {
    font-family: "Montserrat", Arial, sans-serif;
    font-weight: 400;
    letter-spacing: 0.16em;
    text-transform: uppercase;
    white-space: nowrap;
  }
  .card--front .brand {
    position: absolute;
    left: 50%;
    top: 50%;
    transform: translate(-50%, -50%);
  }
  .card--front .brand__name { font-size: 32px; color: var(--brand-grey); }

  .back__band {
    position: absolute;
    left: 0; top: 0;
    width: 100%;
    height: 232px;
    background: var(--band-dark);
  }
  .back__band .brand {
    position: absolute;
    left: 44px;
    top: 100px;
  }
  .back__band .brand__mark { width: 26px; height: 26px; }
  .back__band .brand__name { font-size: 24px; color: var(--ink-light); }
  .person {
    position: absolute;
    right: 48px;
    top: 92px;
    color: var(--ink-light);
  }
  .person__name {
    font-family: "Montserrat", Arial, sans-serif;
    font-size: 24px;
    font-weight: 400;
  }
  .person__title { font-size: 12px; margin-top: 4px; }

  .back__stripe {
    position: absolute;
    left: 0; top: 232px;
    width: 100%;
    height: 20px;
    background: linear-gradient(180deg, var(--gold-light), var(--gold-deep));
    display: flex;
    align-items: center;
    justify-content: center;
  }
  .back__web { font-size: 11px; color: #3a3a2a; letter-spacing: 0.04em; }

  .services {
    position: absolute;
    left: 44px;
    top: 270px;
    list-style: none;
    font-size: 11.5px;
    line-height: 1.5;
    color: var(--ink);
  }
  .contacts {
    position: absolute;
    right: 48px;
    top: 284px;
    font-size: 13px;
    line-height: 1.6;
    color: var(--ink);
  }
</style>
</head>
<body>
  <section class="card card--front" aria-label="Card front">
    <div class="brand">
      <span class="brand__mark"></span>
      <span class="brand__name">Lumavant Studio</span>
    </div>
  </section>

  <section class="card card--back" aria-label="Card back">
    <div class="back__band">
      <div class="brand">
        <span class="brand__mark"></span>
        <span class="brand__name">Lumavant Studio</span>
      </div>
      <div class="person">
        <p class="person__name">Tod Parvin</p>
        <p class="person__title">Founder and CEO</p>
      </div>
    </div>
    <div class="back__stripe"><span class="back__web">lumavantstudio.example</span></div>
    <ul class="services">
      <li>Content &amp; Experience Strategy</li>
      <li>Brand Development</li>
      <li>Search Engine Optimization</li>
      <li>Website Design</li>
      <li>Website Operation</li>
      <li>Social Media Integration</li>
      <li>Complete Video Solutions</li>
    </ul>
    <p class="contacts">
      Mobile 949-628-4513<br>
      Email tod@lumavantstudio.example<br>
      Web lumavantstudio.example
    </p>
  </section>
</body>
</html>
```